Web-Design  für naturwissenschaflich-philosophische Institution
Zielgruppe
Es handelt sich um eine naturwissenschaflich-philosophische Institution. Besucher sind neben Natur- und Geisteswissenschaftlern auch interessierte Laien.
Kernthema der Seite ist alles rund um das Thema Zahlen, allerdings unter einem naturwissenschaftlich, philosophischen Aspekt. Nach einer grundsätzlichen Erklärung (Leitartikel 'Als Flüsse singen') baut die Seite sich auf aus zahreichen Beispielen/Beiträgen aus den unterschiedlichsten Fachbereichen, die scheinbar keinerlei Bezug zueinander haben, wie Mathematik, Geometrie einerseits und der großen Literatur einschließlich historischer und religiöser Schriften andererseits. Immer aber gibt es einen Bezug zu fraktal wachsenden Dreiecken.
Die Artikel sind meist populärwissenschaftlich formuliert. Es handelt sich nicht um esoterische Inhalte, auch wenn der Domainname www.kelmbrauth.de das evtl. vermuten ließe. Keine Berührung zu Spiritualität. Die Institution ist im Aufbau und hat durchaus den Anspruch, diese klassischen Themen modern aufzugreifen. Sie ist nicht verstaubt.
Aufgabenstellung
Geordneter, klarer, transparenter Aufbau. Übersichtlich und strukturiert, wie zB www.qrl.de Es sollten geometrische Proportionen eingehalten werden (wie Symmetrie, goldener Schnitt). Nicht zu viele verschiedene Stilelemente. Die Seite sollte einladend sein, ggf. ansprechendes Bild auf Startseite (mit Bezug zu Zahlen, Geoemetrie).
Die Startseite braucht nun im Header kein Logo mehr zu haben. Der Seitentitel sollte sein 'Das Echo der Wolken'. Siehe Anhang 'Header Beispiel'
Als Menüpunkte benötigen wir neben Home, nur 'Beiträge', 'Buch', 'Kontakt' oder einfach nur die bekannten drei Striche. Der Link zum Impressum genügt im Footer. Rechts oben benötigt man ein Suchfeld.
Besonderheit: Man benötigt eine Art zweiten Header, der aus einer Zahlenreihe besteht. Die einzelnen Zahlen müssen später verlinkt sein auf Unterseiten. Siehe Muster im Anhang. Der User muss sie als Link erkennen können (evtl. Programmierthema: zB Hervorheben beim drüberhoovern). Die Zahlen müssen erweiterbar sein, ggf. über Pfeil klicken, siehe
Es gibt einen zentralen Startartikel. Auf diesen muss man leicht kommen. Im Muster heißt er 'Als die Flüsse singen'.
Das Bild hier ist sehr wichtig. Es sollte bestehn aus vielen interessanten Zahlen, wie in 'Zahlenwolke' angegeben. Und möglichst auch den Dreiecken wie in 'Logo1'.
Weiter unten auf der Startseite sollte es dann weitere Elemente geben, einmal wo man zu bestimmten Unterkategorien kommt, im Muster sind das 'Bibel und Zahlen' 'Naturwissenschaft' etc. und dann evtl weiter unten noch ein Stilelemente, in welchem man die neuesten Artikel verlinken kann.

```html
<!DOCTYPE html>
<html lang="de">
<head>
<meta charset="utf-8">
<title>Das Echo der Wolken</title>
<link href="https://fonts.googleapis.com/css2?family=Poppins:wght@400;500;600;700;800&display=swap" rel="stylesheet">
<style>
:root{
  --stage:#e6e6e6;
  --white:#ffffff;
  --blue:#1a7fe8;
  --blue-deep:#3a82d2;
  --blue-light:#52a6ea;
  --ink:#263448;
  --ink-soft:#3d4652;
  --text-grey:#4c5560;
  --band:#ececec;
  --card:#f2f2f2;
  --line:#c9c9c9;
}
*{box-sizing:border-box;margin:0;padding:0}
html,body{width:1200px;height:2447px;overflow:hidden}
body{background:var(--stage);font-family:"Poppins",sans-serif;color:var(--ink);position:relative}

/* site component */
.site{position:relative;width:1200px;height:1247px;background:var(--white)}
.site-header{position:absolute;left:0;top:0;width:1200px;height:63px;background:var(--white)}
.site-title{position:absolute;left:176px;top:17px;font-size:21px;color:var(--blue);font-weight:400;white-space:nowrap}
.site-title b{font-weight:600}
.main-nav{position:absolute;left:530px;top:24px;display:flex;font-size:11px;font-weight:500;color:var(--ink);letter-spacing:.2px}
.main-nav span{padding:0 12px;border-left:1px solid var(--line);line-height:14px}
.main-nav span:first-child{border-left:0}
.search{position:absolute;left:901px;top:19px;width:124px;height:24px;border:1px solid #8a8f96;border-radius:2px;font-size:10px;color:#c8c8c8;padding:5px 6px}
.search svg{position:absolute;right:6px;top:5px}

.number-bar{position:absolute;left:0;top:63px;width:1200px;height:36px;background:var(--band)}
.number-bar .label{position:absolute;left:623px;top:10px;font-size:12px;font-weight:500;color:var(--ink)}
.number-bar .arrow{position:absolute;top:14px}
.number-bar .prev{left:770px}
.number-bar .next{left:1019px}
.numbers{position:absolute;left:789px;top:9px;display:flex;gap:6px}
.numbers span{width:19px;height:19px;border-radius:3px;background:var(--ink-soft);color:var(--white);font-size:13px;font-weight:600;line-height:19px;text-align:center}
.numbers span.active{background:var(--blue)}

.hero{position:absolute;left:0;top:99px;width:1200px;height:525px;background:radial-gradient(ellipse at 35% 65%,var(--blue-light) 0%,var(--blue-deep) 60%,#3b86d8 100%)}
.hero-title{position:absolute;left:176px;top:166px;font-size:57px;line-height:62px;font-weight:800;color:var(--white);letter-spacing:-.5px}
.hero-button{position:absolute;left:176px;top:319px;width:228px;height:37px;background:#efefef;color:var(--blue);font-size:12px;font-weight:500;text-align:center;line-height:37px}

.topics{position:absolute;left:175px;top:719px;display:flex;gap:24px}
.topic-card{position:relative;width:267px;height:312px;background:var(--card);box-shadow:0 1px 4px rgba(0,0,0,.12);padding:28px 26px}
.topic-card h2{font-size:30px;line-height:35px;font-weight:500;color:var(--ink);overflow-wrap:anywhere;height:82px}
.topic-card p{margin-top:4px;font-size:11.4px;line-height:16px;color:var(--text-grey)}
.topic-card .card-button{position:absolute;left:26px;top:249px;width:140px;height:37px;background:var(--blue);color:var(--white);font-size:12px;font-weight:600;text-align:center;line-height:37px}

.to-top{position:absolute;left:1090px;top:1138px;width:25px;height:25px;background:#eeeeee}
.to-top svg{position:absolute;left:6px;top:7px}
.site-footer{position:absolute;left:0;top:1189px;width:1200px;height:58px;background:var(--band);font-size:12px;color:var(--ink)}
.site-footer .links{position:absolute;left:812px;top:20px;display:flex}
.site-footer .links span{padding:0 17px;border-left:1px solid var(--line);line-height:14px}
.site-footer .links span:first-child{border-left:0;padding-left:0}

/* placements */
.preview{position:absolute;left:369px;top:249px;width:831px;height:647px;overflow:hidden;background:var(--white)}
.preview .site{transform:scale(.833);transform-origin:0 0}
.page{position:absolute;left:0;top:1200px}
</style>
</head>
<body>

<div class="preview" aria-hidden="true">
  <div class="site">
    <header class="site-header">
      <div class="site-title"><b>Das Echo</b> der Wolken</div>
      <nav class="main-nav"><span>HOME</span><span>BETRAGE</span><span>BUCH</span><span>KONTAKT</span><span>IMPRESSUM</span></nav>
      <div class="search">Suche<svg width="12" height="12" viewBox="0 0 12 12"><circle cx="7" cy="5" r="3.6" fill="none" stroke="#333" stroke-width="1.2"/><line x1="4.4" y1="7.6" x2="1" y2="11" stroke="#333" stroke-width="1.2"/></svg></div>
    </header>
    <div class="number-bar">
      <div class="label">und was sie erzählen:</div>
      <svg class="arrow prev" width="6" height="8"><polygon points="6,0 6,8 0,4" fill="var(--ink)"/></svg>
      <div class="numbers"><span class="active">1</span><span>2</span><span>3</span><span>4</span><span>5</span><span>6</span><span>7</span><span>8</span><span>9</span></div>
      <svg class="arrow next" width="6" height="8"><polygon points="0,0 0,8 6,4" fill="var(--blue)"/></svg>
    </div>
    <section class="hero" role="img" aria-label="Zahlenwolke mit Dreiecken aus Zahlen auf blauem Grund">
      <h1 class="hero-title">Als die<br>Flüsse singen ...</h1>
      <div class="hero-button">Lern mehr</div>
    </section>
    <section class="topics">
      <article class="topic-card"></article>
      <article class="topic-card"></article>
      <article class="topic-card"></article>
    </section>
  </div>
</div>

<div class="page">
  <div class="site">
    <header class="site-header">
      <div class="site-title"><b>Das Echo</b> der Wolken</div>
      <nav class="main-nav"><span>HOME</span><span>BETRAGE</span><span>BUCH</span><span>KONTAKT</span><span>IMPRESSUM</span></nav>
      <div class="search">Suche<svg width="12" height="12" viewBox="0 0 12 12"><circle cx="7" cy="5" r="3.6" fill="none" stroke="#333" stroke-width="1.2"/><line x1="4.4" y1="7.6" x2="1" y2="11" stroke="#333" stroke-width="1.2"/></svg></div>
    </header>
    <div class="number-bar">
      <div class="label">und was sie erzählen:</div>
      <svg class="arrow prev" width="6" height="8"><polygon points="6,0 6,8 0,4" fill="var(--ink)"/></svg>
      <div class="numbers"><span class="active">1</span><span>2</span><span>3</span><span>4</span><span>5</span><span>6</span><span>7</span><span>8</span><span>9</span></div>
      <svg class="arrow next" width="6" height="8"><polygon points="0,0 0,8 6,4" fill="var(--blue)"/></svg>
    </div>
    <section class="hero" role="img" aria-label="Zahlenwolke mit Dreiecken aus Zahlen auf blauem Grund">
      <h1 class="hero-title">Als die<br>Flüsse singen ...</h1>
      <div class="hero-button">Lern mehr</div>
    </section>
    <section class="topics">
      <article class="topic-card">
        <h2>Bibel und Zahlen</h2>
        <p>Die Heilige Schrift ist ein Werk aus Zahlen. Ihre Verfasser haben die archetypischen Inhalte in wundersamer Art und Weise in der Bibel. Und so weiter und so fort</p>
        <div class="card-button">Lern mehr</div>
      </article>
      <article class="topic-card">
        <h2>Naturwissenschaft</h2>
        <p>Die Heilige Schrift ist ein Werk aus Zahlen. Ihre Verfasser haben die archetypischen Inhalte in wundersamer Art</p>
        <div class="card-button">Lern mehr</div>
      </article>
      <article class="topic-card">
        <h2>Philosophie</h2>
        <p>Die Heilige Schrift ist ein Werk aus Zahlen. Ihre Verfasser haben die archetypischen Inhalte in wundersamer Art und Weise der Bibel. Und so weiter und so fort und vieles mehr das sehr schön eindrucksvoll ist</p>
        <div class="card-button">Lern mehr</div>
      </article>
    </section>
    <div class="to-top"><svg width="13" height="11"><polygon points="6.5,0 13,11 0,11" fill="#1e2530"/></svg></div>
    <footer class="site-footer">
      <div class="links"><span>Impressum/Datenschutz</span><span>Kontakt</span></div>
    </footer>
  </div>
</div>

</body>
</html>
```